Custom Truck shop New Business Card design

double sided business card including my new logo, brand colors and picking a font I attached, clean and modern look. I attached the old card for some reference. and would like to include the picture of the white truck attached. I would also like to have it with one of my employees info as well. (same info except name and title Brin Tolvay Service Writer)

Dale Porvick
Owner

address
48310 E Calloway Ridge Rd S
STE 217
Marsh Hollow, CO 80219

phone 720-555-0184

email dale@brokenspurrigs.example

website brokenspurrgis.example

social @brokenspurrigs

Target Market(s)

men 18-60

Industry/Entity Type

Automotive

Contact Information for Business Card

Dale Porvick Owner address 48310 E Calloway Ridge Rd S STE 217 Marsh Hollow, CO 80219 phone 720-555-0184 email dale@brokenspurrigs.example website brokenspurrgis.example social @brokenspurrigs

Font styles to use
Other font styles liked:
• fonts attached

Requirements
Must have
• new logo, orange #FC68D, Charcoal #333333
Nice to have
• the white truck

```html
<!DOCTYPE html>
<html lang="en">
<head>
<meta charset="utf-8">
<title>Broken Spur Rigs – Business Card</title>
<link rel="stylesheet" href="https://fonts.googleapis.com/css2?family=Lato:wght@400;700&family=Montserrat:wght@700&display=swap">
<style>
  :root {
    --charcoal: #333333;
    --charcoal-deep: #2b2b2b;
    --orange: #e6622a;
    --white: #f4f4f4;
    --backdrop: #e9e7e4;
  }
  * { box-sizing: border-box; margin: 0; padding: 0; }
  html, body {
    width: 1200px; height: 900px; overflow: hidden;
    background: var(--backdrop);
  }
  .sheet {
    position: relative; width: 1200px; height: 900px;
  }
  .card {
    position: absolute; left: 250px; width: 700px; height: 400px;
    background: var(--charcoal);
    border-radius: 34px 0 34px 0;
    overflow: hidden;
    box-shadow: 0 10px 28px rgba(0,0,0,0.22);
    font-family: "Lato", sans-serif;
    color: var(--white);
  }
  .card--front { top: 30px; }
  .card--back { top: 470px; }

  /* front */
  .photo-edge {
    position: absolute; inset: 0;
    background: var(--orange);
    clip-path: polygon(34.4% 0, 100% 0, 100% 100%, 69.4% 100%);
  }
  .photo {
    position: absolute; inset: 0;
    background: linear-gradient(160deg, #b9bcc0 0%, #7c8a78 30%, #5d6b57 45%, #a9adb2 60%, #4a4a4e 85%, #2d2d30 100%);
    clip-path: polygon(35% 0, 100% 0, 100% 100%, 70% 100%);
  }
  .front-brand {
    position: absolute; left: 40px; top: 150px; width: 300px;
    text-align: center;
  }
  .brand-name {
    font-family: "Montserrat", sans-serif; font-weight: 700;
    color: var(--orange); letter-spacing: 1px; text-transform: uppercase;
  }
  .front-brand .brand-name { font-size: 30px; line-height: 1.15; }
  .rule { height: 2px; background: var(--orange); }
  .front-brand .rule { margin: 14px auto 0; width: 250px; }
  .social {
    position: absolute; left: 40px; top: 305px; width: 300px;
    display: flex; align-items: center; justify-content: center; gap: 8px;
    font-size: 17px;
  }
  .social-dot { width: 12px; height: 12px; border-radius: 50%; background: var(--orange); }

  /* back */
  .person { position: absolute; left: 40px; top: 60px; }
  .person-title { font-size: 17px; color: var(--white); }
  .person-name {
    font-family: "Montserrat", sans-serif; font-weight: 700;
    font-size: 22px; color: var(--orange); text-transform: uppercase; letter-spacing: 0.5px;
  }
  .contact {
    position: absolute; left: 360px; top: 70px; list-style: none;
    font-size: 15.5px; line-height: 1.35;
  }
  .contact li { display: flex; align-items: flex-start; gap: 10px; margin-bottom: 6px; }
  .contact svg { width: 16px; height: 16px; flex: none; margin-top: 2px; fill: var(--orange); }
  .back-brand {
    position: absolute; left: 360px; top: 250px; width: 300px; text-align: center;
  }
  .back-brand .rule { width: 300px; }
  .back-brand .brand-name { font-size: 27px; margin: 12px 0; }
  .back-brand .rule--short { width: 240px; margin: 0 auto; }
</style>
</head>
<body>
<main class="sheet">

  <section class="card card--front" aria-label="Card front">
    <div class="photo-edge"></div>
    <div class="photo" role="img" aria-label="Photo of a lifted white pickup truck on large chrome wheels, parked in front of evergreen trees"></div>
    <div class="front-brand">
      <p class="brand-name">Broken Spur Rigs</p>
      <div class="rule"></div>
    </div>
    <p class="social"><span class="social-dot"></span>@brokenspurrigs</p>
  </section>

  <section class="card card--back" aria-label="Card back">
    <div class="person">
      <p class="person-title">Owner</p>
      <p class="person-name">Dale Porvick</p>
    </div>
    <ul class="contact">
      <li><svg viewBox="0 0 16 16"><path d="M3 1l3 3-1.6 2.2a9 9 0 0 0 5.4 5.4L12 10l3 3-2 2C6.5 15 1 9.5 1 3z"/></svg>720-555-0184</li>
      <li><svg viewBox="0 0 16 16"><path d="M1 3h14v10H1zM2 4.2v.6l6 4 6-4v-.6z"/></svg>dale@brokenspurrigs.example</li>
      <li><svg viewBox="0 0 16 16"><path d="M8 1a7 7 0 1 0 0 14A7 7 0 0 0 8 1zm0 1.5c.8 0 1.7 1.8 2 4.5H6c.3-2.7 1.2-4.5 2-4.5zM2.6 7h2c0-1.6.4-3 .9-3.9A5.5 5.5 0 0 0 2.6 7zm7.9-3.9c.5.9.9 2.3.9 3.9h2a5.5 5.5 0 0 0-2.9-3.9zM2.6 9a5.5 5.5 0 0 0 2.9 3.9c-.5-.9-.9-2.3-.9-3.9zm3.4 0c.3 2.7 1.2 4.5 2 4.5s1.7-1.8 2-4.5zm5.4 0c0 1.6-.4 3-.9 3.9A5.5 5.5 0 0 0 13.4 9z"/></svg>www.brokenspurrgis.example</li>
      <li><svg viewBox="0 0 16 16"><path d="M8 0a5.5 5.5 0 0 0-5.5 5.5C2.5 10 8 16 8 16s5.5-6 5.5-10.5A5.5 5.5 0 0 0 8 0zm0 3.5a2 2 0 1 1 0 4 2 2 0 0 1 0-4z"/></svg><span>48310 E Calloway Ridge Rd S<br>STE 217, Marsh Hollow, CO 80219</span></li>
    </ul>
    <div class="back-brand">
      <div class="rule"></div>
      <p class="brand-name">Broken Spur Rigs</p>
      <div class="rule rule--short"></div>
    </div>
  </section>

</main>
</body>
</html>
```